Design our beautiful and attractive PowerPoint template presentation

As you can see in the files attached below within this brief, we would like pls to receive a proposal for our Drelko Motion Drives a powerpoint template which would include:
- open slide
- agenda slide
- 5 different main chapter slides , for examples below but chapter name shall be replaced according to need:
* about us
* products
* applications
* technical specifications
* testing and benchmark
- Q&A slide
- Conclusion slide
- Closing side
Pls also take a look to the web site being developed (under construction) to ensure you keep the same look and feel: http://drelkomd.quarnet.example/index.php?id=308

Target Market(s)

Industry, multi channels

Industry/Entity Type

B-t-B mechanical parts distributors

Font styles to use
Other font styles liked:
• Pls see the font provided into the brief attached files

Requirements
Must have
• Follow the color, font and logo provided into the brief attached files
Nice to have
• Animated slides

```html
<!DOCTYPE html>
<html lang="en">
<head>
<meta charset="utf-8">
<title>Drelko Motion Drives – Presentation Template</title>
<link href="https://fonts.googleapis.com/css2?family=Open+Sans:ital,wght@0,400;0,600;0,700;1,400&display=swap" rel="stylesheet">
<style>
:root{
  --blue:#1670c7;
  --blue-deep:#0f62b5;
  --blue-soft:#5aa7e3;
  --blue-pale:#d6e7f7;
  --stage:#d5d5d5;
  --ink:#2f2f2f;
  --grey:#8d8d8d;
  --grey-light:#b9bcbf;
  --white:#ffffff;
  --photo:linear-gradient(135deg,#7f8f9d 0%,#cfd6dc 45%,#9aa6ae 70%,#56636f 100%);
}
*{box-sizing:border-box;margin:0;padding:0}
html,body{width:1200px;height:720px;overflow:hidden}
body{background:var(--stage);font-family:"Open Sans",Arial,sans-serif;color:var(--ink);position:relative}
.slide{position:absolute;width:221px;height:125px;background:var(--white);overflow:hidden;box-shadow:0 3px 5px rgba(0,0,0,.28)}
.c1{left:17px}.c2{left:249px}.c3{left:481px}.c4{left:713px}.c5{left:945px}
.r1{top:75px}.r2{top:218px}.r3{top:361px}.r4{top:504px}
.top-bar{position:absolute;top:0;left:66px;width:89px;height:3px;background:var(--blue);clip-path:polygon(0 0,100% 0,96% 100%,4% 100%)}
.footer{position:absolute;left:0;right:0;bottom:0;height:1.6px;background:var(--blue)}
.page-tab{position:absolute;right:6px;bottom:0;width:22px;height:5px;background:var(--white);font-size:3px;color:var(--blue);text-align:center;line-height:4px;clip-path:polygon(15% 0,100% 0,100% 100%,0 100%)}
.page-tab::before{content:"";position:absolute;left:-30px;right:0;bottom:0;height:1.6px;background:var(--blue)}
.headline{position:absolute;top:8px;left:0;right:0;text-align:center;font-size:6.4px;font-weight:700;color:var(--blue);line-height:1}
.subline{position:absolute;top:16px;left:0;right:0;text-align:center;font-size:4.6px;line-height:1}
.dots{position:absolute;top:24px;left:50%;transform:translateX(-50%);display:flex;gap:1.3px}
.dots i{width:2.6px;height:2.6px;border-radius:50%;background:var(--blue);display:block}
.dots i:nth-child(3){background:var(--blue-soft)}.dots i:nth-child(4){background:var(--blue-pale)}
.txt{position:absolute;font-size:2.9px;line-height:1.45;color:var(--ink)}
.txt b{font-weight:600}
.txt em{display:block;color:var(--blue);font-style:italic}
.photo{position:absolute;background:var(--photo)}
/* cover */
.cover-brand{position:absolute;left:13px;top:12px;font-size:7px;font-weight:700;color:var(--white);line-height:1.1;width:80px}
.cover-title{position:absolute;right:12px;top:73px;text-align:right;font-size:10.4px;line-height:1.35;color:var(--blue)}
.cover-note{position:absolute;right:12px;top:104px;font-size:4px;color:var(--grey-light)}
/* agenda */
.agenda-title{position:absolute;left:20px;top:55px;width:44px;text-align:right;font-size:6px;font-weight:700;color:var(--blue);line-height:1.45}
.agenda-dots{top:82px;left:47px;transform:none}
.agenda-rule{position:absolute;left:73px;top:14px;width:.6px;height:100px;background:var(--grey-light)}
.agenda-item{position:absolute;left:76px;width:138px;height:22px}
.num{position:absolute;left:0;top:1px;width:15px;height:15px;border-radius:50%;border:1px solid var(--blue-pale);background:var(--white);color:var(--blue);font-size:9px;font-weight:600;text-align:center;line-height:13px}
.agenda-item .txt{left:19px;top:0;width:118px}
/* stats */
.stat-row{position:absolute;left:8px;width:134px;height:16px;border-bottom:.5px solid var(--grey-light)}
.stat-row .txt{left:0;top:0;width:130px}
.pct{position:absolute;left:145px;width:16px;height:15px;background:var(--grey);color:var(--white);font-size:5.6px;text-align:center;line-height:15px}
.stat-panel{position:absolute;left:163px;top:30px;width:52px;height:88px;background:var(--blue-deep);color:var(--white);padding:3px}
.stat-panel .txt{position:static;color:var(--white)}
.stat-panel ul{margin-top:2px;list-style:none}
.stat-panel li{font-size:2.9px;line-height:1.5}
.stat-panel li::before{content:"● ";font-size:2.4px}
/* table */
.grid-table{position:absolute;left:10px;top:49px;width:201px;border-collapse:collapse}
.grid-table td{border:.5px solid var(--blue-soft);height:7.6px;background:var(--white)}
.grid-table tr:first-child td{background:var(--blue-soft)}
.grid-table tr:nth-child(odd):not(:first-child) td{background:var(--blue-pale)}
/* placeholder */
.placeholder{position:absolute;left:10px;top:34px;width:101px;height:71px;background:#636363;color:var(--white);font-size:10px;display:flex;align-items:center;justify-content:center}
/* chevrons */
.chevron{position:absolute;top:37px;width:34px;height:72px;background:var(--blue);clip-path:polygon(0 0,100% 14%,100% 86%,0 100%);color:var(--white);text-align:center;padding:15px 3px 0}
.chevron b{display:block;font-size:3.4px;font-weight:400;margin-bottom:2px}
.chevron span{display:block;font-size:2.6px;line-height:1.35}
/* team rows */
.team-cell{position:absolute;width:104px;height:27px}
.team-cell .photo{left:0;top:0;width:40px;height:26px}
.team-cell .txt{left:44px;top:0;width:58px}
/* steps */
.step-band{position:absolute;left:0;right:0;top:44px;height:14px;background:var(--grey-light)}
.step-num{position:absolute;top:43px;width:16px;height:16px;border-radius:50%;background:var(--blue);border:1.2px solid var(--white);color:var(--white);font-size:7px;font-weight:600;text-align:center;line-height:13.5px}
.step-label{position:absolute;top:67px;width:56px;text-align:center;font-size:3px;color:var(--blue-soft)}
.step-text{text-align:center;width:60px;top:74px}
/* hero */
.hero-panel{position:absolute;left:16px;top:0;width:74px;height:112px;background:var(--blue-deep);color:var(--white);padding:12px 6px 0}
.hero-panel h2{font-size:6.4px;font-weight:700;line-height:1}
.hero-panel p.lead{font-size:4.6px;line-height:1.3;color:#cfe3f7;margin:4px 0 4px}
.hero-panel .txt{position:static;color:var(--white);font-size:2.6px;line-height:1.35}
/* hex */
.hex-label{font-size:5px;fill:var(--ink);font-family:"Open Sans",Arial,sans-serif}
.hex-in{font-size:5px;fill:var(--blue);font-family:"Open Sans",Arial,sans-serif}
/* closing */
.close-brand{position:absolute;left:10px;top:104px;font-size:6px;font-weight:700;color:var(--white);line-height:1.1;width:52px}
.close-contact{position:absolute;left:63px;top:101px;font-size:2.8px;line-height:1.45;color:var(--white)}
/* gallery */
.gallery-cell{position:absolute;width:47px}
.gallery-cell .photo{position:relative;display:block;width:47px;height:29px}
.gallery-cell span{display:block;font-size:2.6px;margin-top:2px;color:var(--ink)}
.gallery-cell span::before{content:"";display:inline-block;width:2px;height:2px;background:var(--blue);margin-right:2px}
.chart-label{font-family:"Open Sans",Arial,sans-serif;font-size:3px;fill:#555}
</style>
</head>
<body>

<!-- 1 cover -->
<section class="slide c1 r1">
  <svg width="221" height="125" style="position:absolute;left:0;top:0">
    <polygon points="0,0 221,0 221,32 0,86" fill="var(--blue)"/>
    <polygon points="0,86 221,32 221,37 0,92" fill="var(--grey-light)"/>
  </svg>
  <div class="cover-brand">Drelko Motion Drives</div>
  <div class="cover-title">YOUR HEADLINE TEXT<br>HERE TO PUT</div>
  <div class="cover-note">LOREM IPSUM IS SIMPLY DUMMY HAS BEEN</div>
</section>

<!-- 2 agenda -->
<section class="slide c2 r1">
  <div class="top-bar"></div>
  <div class="agenda-title">YOUR<br>HEADLINE<br>HERE</div>
  <div class="dots agenda-dots"><i></i><i></i><i></i><i></i></div>
  <div class="agenda-rule"></div>
  <div class="agenda-item" style="top:14px"><div class="num">1</div><p class="txt"><em style="font-style:normal">Drive range built in stages</em>Our drive units are built in stages to match the load, speed and duty cycle of each line.</p></div>
  <div class="agenda-item" style="top:40px"><div class="num">2</div><p class="txt"><em style="font-style:normal">Drive range built in stages</em>Our drive units are built in stages to match the load, speed and duty cycle of each line.</p></div>
  <div class="agenda-item" style="top:66px"><div class="num">3</div><p class="txt"><em style="font-style:normal">Drive range built in stages</em>Our drive units are built in stages to match the load, speed and duty cycle of each line.</p></div>
  <div class="agenda-item" style="top:93px"><div class="num">4</div><p class="txt"><em style="font-style:normal">Drive range built in stages</em>Our drive units are built in stages to match the load, speed and duty cycle of each line.</p></div>
  <div class="page-tab">12</div>
</section>

<!-- 3 two columns -->
<section class="slide c3 r1">
  <div class="top-bar"></div>
  <h1 class="headline">YOUR HEADLINE HERE</h1><p class="subline">Lorem ipsum is simply dummy has been</p>
  <div class="dots"><i></i><i></i><i></i><i></i></div>
  <p class="txt" style="left:10px;top:35px;width:98px">Automated drive control<br>Our drive units are built in stages to match the load, speed and duty cycle of each line. Every gearbox is tested on the bench before it ships, so partners can fit it with full trust. Distributors order stock through one portal, track each batch and get parts to the plant fast. Our drive units are built in stages to match the load, speed and duty cycle of each line. Every gearbox is tested on the bench before it ships, so partners can fit it with full trust. Distributors order stock through one portal, track each batch and get parts to the plant fast.</p>
  <p class="txt" style="left:114px;top:35px;width:98px;border-left:.4px solid var(--grey-light);padding-left:3px">value<em>Certified gearbox line and test reports</em>Our drive units are built in stages to match the load, speed and duty cycle of each line. Every gearbox is tested on the bench before it ships, so partners can fit it with full trust. Distributors order stock through one portal, track each batch and get parts to the plant fast. Our drive units are built in stages to match the load, speed and duty cycle of each line. Every gearbox is tested on the bench before it ships, so partners can fit it with full trust. Distributors order stock through one portal, track each batch and get parts to the plant fast.</p>
  <div class="page-tab">12</div>
</section>

<!-- 4 stats -->
<section class="slide c4 r1">
  <div class="top-bar"></div>
  <h1 class="headline">YOUR HEADLINE HERE</h1><p class="subline">Lorem ipsum is simply dummy has been</p>
  <div class="dots"><i></i><i></i><i></i><i></i></div>
  <div class="stat-row" style="top:30px"><p class="txt">Our drive units are built in stages to match the load, speed and duty cycle of each line.</p></div>
  <div class="stat-row" style="top:48px"><p class="txt">Our drive units are built in stages to match the load, speed and duty cycle of each line.</p></div>
  <div class="stat-row" style="top:66px"><p class="txt">Our drive units are built in stages to match the load, speed and duty cycle of each line.</p></div>
  <div class="stat-row" style="top:84px"><p class="txt">Our drive units are built in stages to match the load, speed and duty cycle of each line.</p></div>
  <div class="stat-row" style="top:102px"><p class="txt">Our drive units are built in stages to match the load, speed and duty cycle of each line.</p></div>
  <div class="pct" style="top:31px">50%</div><div class="pct" style="top:48px">10%</div><div class="pct" style="top:66px">15%</div><div class="pct" style="top:84px">25%</div><div class="pct" style="top:102px">65%</div>
  <div class="stat-panel">
    <p class="txt">Distributors order stock through one portal, track each batch and get parts to the plant fast.</p>
    <ul><li>Fast stock checks</li><li>Bench tested units</li><li>One order portal</li></ul>
  </div>
  <div class="page-tab">12</div>
</section>

<!-- 5 bar chart -->
<section class="slide c5 r1">
  <div class="top-bar"></div>
  <h1 class="headline">YOUR HEADLINE HERE</h1><p class="subline">Lorem ipsum is simply dummy has been</p>
  <div class="dots"><i></i><i></i><i></i><i></i></div>
  <svg width="221" height="100" style="position:absolute;left:0;top:25px">
    <text x="110" y="12" text-anchor="middle" class="chart-label" style="font-size:3.4px">Chart Title</text>
    <line x1="52" y1="85" x2="170" y2="85" stroke="#ccc" stroke-width=".4"/>
    <g>
      <rect x="59" y="43" width="5" height="42" fill="var(--blue)"/><rect x="65" y="61" width="5" height="24" fill="var(--blue-soft)"/><rect x="71" y="55" width="5" height="30" fill="var(--grey)"/>
      <rect x="89" y="54" width="5" height="31" fill="var(--blue)"/><rect x="95" y="40" width="5" height="45" fill="var(--blue-soft)"/><rect x="101" y="62" width="5" height="23" fill="var(--grey)"/>
      <rect x="119" y="51" width="5" height="34" fill="var(--blue)"/><rect x="125" y="67" width="5" height="18" fill="var(--blue-soft)"/><rect x="131" y="58" width="5" height="27" fill="var(--grey)"/>
      <rect x="149" y="41" width="5" height="44" fill="var(--blue)"/><rect x="155" y="57" width="5" height="28" fill="var(--blue-soft)"/><rect x="161" y="33" width="5" height="52" fill="var(--grey)"/>
    </g>
    <text x="67" y="90" text-anchor="middle" class="chart-label">Category 1</text><text x="97" y="90" text-anchor="middle" class="chart-label">Category 2</text><text x="127" y="90" text-anchor="middle" class="chart-label">Category 3</text><text x="157" y="90" text-anchor="middle" class="chart-label">Category 4</text>
    <text x="110" y="95" text-anchor="middle" class="chart-label" style="font-size:2.4px">■ Series 1  ■ Series 2  ■ Series 3</text>
  </svg>
  <div class="page-tab">12</div>
</section>

<!-- 6 table -->
<section class="slide c1 r2">
  <div class="top-bar"></div>
  <h1 class="headline">YOUR HEADLINE HERE</h1><p class="subline">Lorem ipsum is simply dummy has been</p>
  <div class="dots"><i></i><i></i><i></i><i></i></div>
  <p class="txt" style="left:10px;top:34px;width:201px">Our drive units are built in stages to match the load, speed and duty cycle of each line. Every gearbox is tested on the bench before it ships, so partners can fit it with full trust.</p>
  <table class="grid-table">
    <tr><td></td><td></td><td></td></tr><tr><td></td><td></td><td></td></tr><tr><td></td><td></td><td></td></tr><tr><td></td><td></td><td></td></tr><tr><td></td><td></td><td></td></tr><tr><td></td><td></td><td></td></tr><tr><td></td><td></td><td></td></tr><tr><td></td><td></td><td></td></tr>
  </table>
  <div class="page-tab">12</div>
</section>

<!-- 7 image + text -->
<section class="slide c2 r2">
  <div class="top-bar"></div>
  <h1 class="headline">YOUR HEADLINE HERE</h1><p class="subline">Lorem ipsum is simply dummy has been</p>
  <div class="dots"><i></i><i></i><i></i><i></i></div>
  <div class="placeholder">Image</div>
  <p class="txt" style="left:115px;top:34px;width:100px"><em>Certified gearbox line and test reports</em>Our drive units are built in stages to match the load, speed and duty cycle of each line. Every gearbox is tested on the bench before it ships, so partners can fit it with full trust. Distributors order stock through one portal, track each batch and get parts to the plant fast. Our drive units are built in stages to match the load, speed and duty cycle of each line. Every gearbox is tested on the bench before it ships, so partners can fit it with full trust. Distributors order stock through one portal, track each batch and get parts to the plant fast.</p>
  <div class="page-tab">12</div>
</section>

<!-- 8 text -->
<section class="slide c3 r2">
  <div class="top-bar"></div>
  <h1 class="headline">YOUR HEADLINE HERE</h1><p class="subline">Lorem ipsum is simply dummy has been</p>
  <div class="dots"><i></i><i></i><i></i><i></i></div>
  <p class="txt" style="left:9px;top:31px;width:204px"><em>Automated drive control</em>Our drive units are built in stages to match the load, speed and duty cycle of each line. Every gearbox is tested on the bench before it ships, so partners can fit it with full trust. Distributors order stock through one portal, track each batch and get parts to the plant fast. Distributors order stock through one portal, track each batch and get parts to the plant fast.</p>
  <p class="txt" style="left:9px;top:70px;width:204px"><em>Certified gearbox line and test reports</em>Our drive units are built in stages to match the load, speed and duty cycle of each line. Every gearbox is tested on the bench before it ships, so partners can fit it with full trust. Distributors order stock through one portal, track each batch and get parts to the plant fast. Our drive units are built in stages to match the load, speed and duty cycle of each line.</p>
  <div class="page-tab">12</div>
</section>

<!-- 9 chevrons -->
<section class="slide c4 r2">
  <div class="top-bar"></div>
  <h1 class="headline">YOUR HEADLINE HERE</h1><p class="subline">Lorem ipsum is simply dummy has been</p>
  <div class="dots"><i></i><i></i><i></i><i></i></div>
  <div class="chevron" style="left:9px"><b>Text Here</b><span>Compact drive, sealed and ready for heavy duty</span></div>
  <div class="chevron" style="left:45px"><b>Text Here</b><span>Compact drive, sealed and ready for heavy duty</span></div>
  <div class="chevron" style="left:81px"><b>Text Here</b><span>Compact drive, sealed and ready for heavy duty</span></div>
  <p class="txt" style="left:134px;top:34px;width:80px">Our drive units are built in stages to match the load, speed and duty cycle of each line. Every gearbox is tested on the bench before it ships, so partners can fit it with full trust. Distributors order stock through one portal, track each batch and get parts to the plant fast.<em style="margin-top:2px">Certified gearbox line and test reports</em>Every gearbox is tested on the bench before it ships, so partners can fit it with full trust.</p>
  <div class="page-tab">12</div>
</section>

<!-- 10 team grid -->
<section class="slide c5 r2">
  <div class="top-bar"></div>
  <h1 class="headline">YOUR HEADLINE HERE</h1><p class="subline">Lorem ipsum is simply dummy has been</p>
  <div class="dots"><i></i><i></i><i></i><i></i></div>
  <div class="team-cell" style="left:8px;top:30px"><div class="photo" role="img" aria-label="Team photo: colleagues walking through a modern office"></div><p class="txt">Sealed drive units ready for heavy duty use across busy plant lines and long shifts.</p></div>
  <div class="team-cell" style="left:119px;top:30px"><div class="photo" role="img" aria-label="Team photo: colleagues walking through a modern office"></div><p class="txt">Sealed drive units ready for heavy duty use across busy plant lines and long shifts.</p></div>
  <div class="team-cell" style="left:8px;top:60px"><div class="photo" role="img" aria-label="Team photo: colleagues walking through a modern office"></div><p class="txt">Sealed drive units ready for heavy duty use across busy plant lines and long shifts.</p></div>
  <div class="team-cell" style="left:119px;top:60px"><div class="photo" role="img" aria-label="Team photo: colleagues walking through a modern office"></div><p class="txt">Sealed drive units ready for heavy duty use across busy plant lines and long shifts.</p></div>
  <div class="team-cell" style="left:8px;top:90px"><div class="photo" role="img" aria-label="Team photo: colleagues walking through a modern office"></div><p class="txt">Sealed drive units ready for heavy duty use across busy plant lines and long shifts.</p></div>
  <div class="team-cell" style="left:119px;top:90px"><div class="photo" role="img" aria-label="Team photo: colleagues walking through a modern office"></div><p class="txt">Sealed drive units ready for heavy duty use across busy plant lines and long shifts.</p></div>
  <div class="page-tab">12</div>
</section>

<!-- 11 monthly bars -->
<section class="slide c1 r3">
  <div class="top-bar"></div>
  <h1 class="headline">YOUR HEADLINE HERE</h1><p class="subline">Lorem ipsum is simply dummy has been</p>
  <div class="dots"><i></i><i></i><i></i><i></i></div>
  <svg width="140" height="100" style="position:absolute;left:0;top:25px">
    <g fill="#3c8ad4">
      <rect x="14" y="52" width="9" height="40"/><rect x="24" y="43" width="9" height="49"/><rect x="34" y="59" width="9" height="33"/><rect x="44" y="74" width="9" height="18"/><rect x="54" y="88" width="9" height="4"/><rect x="64" y="82" width="9" height="10"/><rect x="74" y="82" width="9" height="10"/><rect x="84" y="77" width="9" height="15"/><rect x="94" y="74" width="9" height="18"/><rect x="104" y="56" width="9" height="36"/><rect x="114" y="49" width="9" height="43"/><rect x="124" y="35" width="9" height="57"/>
    </g>
    <g class="chart-label" text-anchor="middle" style="font-size:2.6px">
      <text x="18" y="50">120</text><text x="28" y="41">146</text><text x="38" y="57">98</text><text x="48" y="72">53</text><text x="58" y="86">11</text><text x="68" y="80">30.3</text><text x="78" y="80">29.9</text><text x="88" y="75">45</text><text x="98" y="72">55</text><text x="108" y="54">109</text><text x="118" y="47">129</text><text x="128" y="33">169</text>
      <text x="18" y="96">Jan</text><text x="28" y="96">Feb</text><text x="38" y="96">Mar</text><text x="48" y="96">Apr</text><text x="58" y="96">May</text><text x="68" y="96">Jun</text><text x="78" y="96">Jul</text><text x="88" y="96">Aug</text><text x="98" y="96">Sep</text><text x="108" y="96">Oct</text><text x="118" y="96">Nov</text><text x="128" y="96">Dec</text>
    </g>
  </svg>
  <p class="txt" style="left:140px;top:29px;width:74px">Our drive units are built in stages to match the load, speed and duty cycle of each line. Every gearbox is tested on the bench before it ships, so partners can fit it with full trust. Distributors order stock through one portal, track each batch and get parts to the plant fast.<em style="margin-top:2px">Certified gearbox line and test reports</em>Each unit ships with a test report.</p>
  <div class="page-tab">12</div>
</section>

<!-- 12 steps -->
<section class="slide c2 r3">
  <div class="top-bar"></div>
  <h1 class="headline">YOUR HEADLINE HERE</h1><p class="subline">Lorem ipsum is simply dummy has been</p>
  <div class="dots"><i></i><i></i><i></i><i></i></div>
  <p class="txt" style="left:10px;top:31px;width:201px;text-align:center">Our drive units are built in stages to match the load, speed and duty cycle of each line. Every gearbox is tested on the bench before it ships, so partners can fit it with full trust.</p>
  <div class="step-band"></div>
  <div class="step-num" style="left:32px">1</div><div class="step-num" style="left:102px">2</div><div class="step-num" style="left:172px">3</div>
  <p class="step-label" style="left:12px">Drive builds</p><p class="step-label" style="left:82px">Drive builds</p><p class="step-label" style="left:152px">Drive builds</p>
  <p class="txt step-text" style="left:10px">Distributors order stock through one portal, track each batch and get parts to the plant fast.</p>
  <p class="txt step-text" style="left:80px">Distributors order stock through one portal, track each batch and get parts to the plant fast.</p>
  <p class="txt step-text" style="left:150px">Distributors order stock through one portal, track each batch and get parts to the plant fast.</p>
  <div class="page-tab">12</div>
</section>

<!-- 13 photo + text -->
<section class="slide c3 r3">
  <div class="top-bar"></div>
  <h1 class="headline">YOUR HEADLINE HERE</h1><p class="subline">Lorem ipsum is simply dummy has been</p>
  <div class="dots"><i></i><i></i><i></i><i></i></div>
  <div class="photo" style="left:10px;top:35px;width:58px;height:67px" role="img" aria-label="Photo: team member standing in a bright office"></div>
  <p class="txt" style="left:76px;top:36px;width:138px">Automated drive control<br>Our drive units are built in stages to match the load, speed and duty cycle of each line. Every gearbox is tested on the bench before it ships, so partners can fit it with full trust. Distributors order stock through one portal, track each batch and get parts to the plant fast. Our drive units are built in stages to match the load, speed and duty cycle of each line. Every gearbox is tested on the bench before it ships, so partners can fit it with full trust. Distributors order stock through one portal, track each batch and get parts to the plant fast.<em>Certified gearbox line and test reports</em>Every gearbox is tested on the bench before it ships, so partners can fit it with full trust.</p>
  <div class="page-tab">12</div>
</section>

<!-- 14 hero -->
<section class="slide c4 r3">
  <div class="photo" style="left:0;top:32px;width:221px;height:93px" role="img" aria-label="Photo: business team walking together through an office"></div>
  <div class="hero-panel">
    <h2>YOUR HEADLINE</h2>
    <p class="lead">Lorem ipsum is simply dummy has been</p>
    <p class="txt">Our drive units are built in stages to match the load, speed and duty cycle of each line. Every gearbox is tested on the bench before it ships, so partners can fit it with full trust. Distributors order stock through one portal, track each batch and get parts to the plant fast. Our drive units are built in stages to match the load, speed and duty cycle of each line. Every gearbox is tested on the bench before it ships, so partners can fit it with full trust. Distributors order stock through one portal, track each batch and get parts to the plant fast.</p>
  </div>
  <div class="page-tab">12</div>
</section>

<!-- 15 hexagons -->
<section class="slide c5 r3">
  <div class="top-bar"></div>
  <h1 class="headline">YOUR HEADLINE HERE</h1><p class="subline">Lorem ipsum is simply dummy has been</p>
  <div class="dots"><i></i><i></i><i></i><i></i></div>
  <svg width="100" height="125" style="position:absolute;left:0;top:0">
    <defs><polygon id="hex" points="0,-12 10.4,-6 10.4,6 0,12 -10.4,6 -10.4,-6"/></defs>
    <use href="#hex" x="34" y="50" fill="var(--blue)"/>
    <use href="#hex" x="57" y="50" fill="var(--white)" stroke="var(--blue)" stroke-width="1"/>
    <use href="#hex" x="45" y="70" fill="var(--white)" stroke="var(--blue)" stroke-width="1"/>
    <use href="#hex" x="68" y="70" fill="var(--blue)"/>
    <use href="#hex" x="34" y="90" fill="var(--blue)"/>
    <use href="#hex" x="57" y="90" fill="var(--white)" stroke="var(--blue)" stroke-width="1"/>
    <text x="57" y="52" text-anchor="middle" class="hex-in">[Text]</text>
    <text x="45" y="72" text-anchor="middle" class="hex-in">[Text]</text>
    <text x="57" y="92" text-anchor="middle" class="hex-in">[Text]</text>
    <text x="16" y="72" text-anchor="middle" class="hex-label">[Text]</text>
    <text x="87" y="92" text-anchor="middle" class="hex-label">[Text]</text>
  </svg>
  <p class="txt" style="left:100px;top:36px;width:114px">Our drive units are built in stages to match the load, speed and duty cycle of each line. Every gearbox is tested on the bench before it ships, so partners can fit it with full trust. Distributors order stock through one portal, track each batch and get parts to the plant fast.<em style="margin-top:2px">Certified gearbox line and test reports</em>Our drive units are built in stages to match the load, speed and duty cycle of each line. Every gearbox is tested on the bench before it ships, so partners can fit it with full trust. Distributors order stock through one portal, track each batch and get parts to the plant fast.</p>
  <div class="page-tab">12</div>
</section>

<!-- 16 two photos -->
<section class="slide c1 r4">
  <div class="top-bar"></div>
  <h1 class="headline">YOUR HEADLINE HERE</h1><p class="subline">Lorem ipsum is simply dummy has been</p>
  <div class="dots"><i></i><i></i><i></i><i></i></div>
  <div class="photo" style="left:9px;top:35px;width:46px;height:67px" role="img" aria-label="Photo: two colleagues walking in an office"></div>
  <p class="txt" style="left:59px;top:35px;width:50px">Automated drive control<br>Our drive units are built in stages to match the load, speed and duty cycle of each line. Every gearbox is tested on the bench before it ships, so partners can fit it with full trust.</p>
  <div class="photo" style="left:113px;top:35px;width:46px;height:67px" role="img" aria-label="Photo: two colleagues walking in an office"></div>
  <p class="txt" style="left:163px;top:35px;width:50px">Automated drive control<br>Our drive units are built in stages to match the load, speed and duty cycle of each line. Every gearbox is tested on the bench before it ships, so partners can fit it with full trust.</p>
  <div class="page-tab">12</div>
</section>

<!-- 17 one photo -->
<section class="slide c2 r4">
  <div class="top-bar"></div>
  <h1 class="headline">YOUR HEADLINE HERE</h1><p class="subline">Lorem ipsum is simply dummy has been</p>
  <div class="dots"><i></i><i></i><i></i><i></i></div>
  <div class="photo" style="left:9px;top:35px;width:79px;height:67px" role="img" aria-label="Photo: business team walking together through an office"></div>
  <p class="txt" style="left:122px;top:35px;width:92px">Automated drive control<br>Our drive units are built in stages to match the load, speed and duty cycle of each line. Every gearbox is tested on the bench before it ships, so partners can fit it with full trust. Distributors order stock through one portal, track each batch and get parts to the plant fast. Our drive units are built in stages to match the load, speed and duty cycle of each line.</p>
  <div class="page-tab">12</div>
</section>

<!-- 18 closing -->
<section class="slide c3 r4">
  <svg width="221" height="125" style="position:absolute;left:0;top:0">
    <polygon points="0,92 221,10 221,125 0,125" fill="var(--blue)"/>
    <polygon points="0,86 221,4 221,10 0,92" fill="var(--grey-light)"/>
  </svg>
  <div class="close-brand">Drelko Motion Drives</div>
  <div class="close-contact">T: +000 555 0142<br>E: hello@drelkomd.example<br>P.O. Box 1200, Harbor Lane<br>Harbor 0000, Australia</div>
</section>

<!-- 19 gallery -->
<section class="slide c4 r4">
  <div class="top-bar"></div>
  <h1 class="headline">YOUR HEADLINE HERE</h1><p class="subline">Lorem ipsum is simply dummy has been</p>
  <div class="dots"><i></i><i></i><i></i><i></i></div>
  <div class="gallery-cell" style="left:9px;top:32px"><div class="photo" role="img" aria-label="Photo: team in an office"></div><span>Sample product title</span></div>
  <div class="gallery-cell" style="left:61px;top:32px"><div class="photo" role="img" aria-label="Photo: team in an office"></div><span>Sample product title</span></div>
  <div class="gallery-cell" style="left:114px;top:32px"><div class="photo" role="img" aria-label="Photo: team in an office"></div><span>Sample product title</span></div>
  <div class="gallery-cell" style="left:166px;top:32px"><div class="photo" role="img" aria-label="Photo: team in an office"></div><span>Sample product title</span></div>
  <div class="gallery-cell" style="left:9px;top:80px"><div class="photo" role="img" aria-label="Photo: team in an office"></div><span>Sample product title</span></div>
  <div class="gallery-cell" style="left:61px;top:80px"><div class="photo" role="img" aria-label="Photo: team in an office"></div><span>Sample product title</span></div>
  <div class="gallery-cell" style="left:114px;top:80px"><div class="photo" role="img" aria-label="Photo: team in an office"></div><span>Sample product title</span></div>
  <div class="gallery-cell" style="left:166px;top:80px"><div class="photo" role="img" aria-label="Photo: team in an office"></div><span>Sample product title</span></div>
  <div class="page-tab">12</div>
</section>

<!-- 20 pie -->
<section class="slide c5 r4">
  <div class="top-bar"></div>
  <h1 class="headline">YOUR HEADLINE HERE</h1><p class="subline">Lorem ipsum is simply dummy has been</p>
  <div class="dots"><i></i><i></i><i></i><i></i></div>
  <svg width="110" height="125" style="position:absolute;left:0;top:0">
    <text x="55" y="42" text-anchor="middle" class="chart-label">Sales</text>
    <path d="M55 72 L55 46 A26 26 0 1 1 41.2 94 Z" fill="var(--blue-deep)"/>
    <path d="M55 72 L41.2 94 A26 26 0 0 1 32.95 58.22 Z" fill="#ee7d22"/>
    <path d="M55 72 L32.95 58.22 A26 26 0 0 1 42.8 49 Z" fill="#a5a5a5"/>
    <path d="M55 72 L42.8 49 A26 26 0 0 1 55 46 Z" fill="#f5be19"/>
    <text x="55" y="106" text-anchor="middle" class="chart-label" style="font-size:2.4px">■ 1st Qtr ■ 2nd Qtr ■ 3rd Qtr ■ 4th Qtr</text>
  </svg>
  <p class="txt" style="left:108px;top:32px;width:106px">Our drive units are built in stages to match the load, speed and duty cycle of each line. Every gearbox is tested on the bench before it ships, so partners can fit it with full trust. Distributors order stock through one portal, track each batch and get parts to the plant fast.<em style="margin-top:2px">Certified gearbox line and test reports</em>Our drive units are built in stages to match the load, speed and duty cycle of each line. Every gearbox is tested on the bench before it ships, so partners can fit it with full trust. Distributors order stock through one portal, track each batch and get parts to the plant fast.</p>
  <div class="page-tab">12</div>
</section>

</body>
</html>
```